Business Card for Web Design consulting firm

Business card designs for Web Design consulting firm

Target Market(s)

English speaking adults ages 30 - 60. Predominantly professional services eg. Doctor, Dentist

Industry/Entity Type

Consulting

Requirements
Must have
• Double sided card

```html
<!DOCTYPE html>
<html lang="en">
<head>
<meta charset="utf-8">
<title>Lumora – Business Card</title>
<link rel="stylesheet" href="https://fonts.googleapis.com/css2?family=Quicksand:wght@700&display=swap">
<style>
  :root {
    --charcoal: #464646;
    --amber: #f4991f;
    --amber-deep: #c27c2c;
    --umber: #6a5b4b;
    --ink: #111111;
    --paper: #ececec;
    --gold: #f7c20c;
    --shadow-dark: rgba(40, 30, 20, 0.85);
  }

  html, body {
    margin: 0;
    padding: 0;
    width: 1200px;
    height: 865px;
    overflow: hidden;
    background: #ffffff;
  }

  .card {
    position: relative;
    width: 1200px;
    height: 865px;
    overflow: hidden;
    font-family: "Quicksand", "Arial Rounded MT Bold", sans-serif;
    font-weight: 700;
    background:
      radial-gradient(ellipse 420px 360px at 0% 0%, rgba(60, 60, 60, 0.9), rgba(60, 60, 60, 0) 100%),
      radial-gradient(ellipse 380px 300px at 100% 100%, rgba(95, 85, 72, 0.95), rgba(95, 85, 72, 0) 100%),
      linear-gradient(125deg, var(--charcoal) 0%, var(--amber-deep) 30%, var(--amber) 52%, var(--amber) 78%, var(--umber) 100%);
  }

  .brand {
    position: absolute;
    left: 84px;
    top: 150px;
    width: 326px;
    display: flex;
    align-items: center;
    gap: 14px;
  }

  .brand-dot {
    flex: none;
    width: 44px;
    height: 44px;
    border-radius: 50%;
    background: var(--amber);
  }

  .brand-name {
    font-size: 56px;
    line-height: 1;
    letter-spacing: 3px;
    color: var(--paper);
    white-space: nowrap;
  }

  .brand-url {
    position: absolute;
    left: 100px;
    top: 246px;
    margin: 0;
    font-size: 30px;
    color: var(--ink);
    letter-spacing: 0.5px;
    white-space: nowrap;
  }

  .tagline {
    position: absolute;
    left: 423px;
    top: 88px;
    margin: 0;
    font-size: 60px;
    line-height: 1.2;
    color: var(--paper);
    text-shadow: 3px 4px 0 var(--shadow-dark);
    white-space: nowrap;
  }

  .person-name {
    position: absolute;
    left: 0;
    right: 80px;
    top: 318px;
    margin: 0;
    text-align: center;
    font-size: 100px;
    line-height: 1.2;
    color: var(--ink);
    text-shadow: 4px 5px 0 rgba(120, 70, 20, 0.75);
  }

  .contact {
    font-size: 42px;
    color: var(--gold);
    text-shadow: 3px 3px 0 var(--shadow-dark);
    white-space: nowrap;
  }

  .address {
    position: absolute;
    left: 71px;
    top: 535px;
    margin: 0;
    font-style: normal;
  }

  .address span {
    display: block;
    line-height: 55px;
  }

  .phone {
    position: absolute;
    left: 71px;
    top: 740px;
    margin: 0;
    line-height: 55px;
  }

  .email {
    position: absolute;
    right: 76px;
    top: 740px;
    margin: 0;
    line-height: 55px;
  }
</style>
</head>
<body>
  <main class="card">
    <div class="brand">
      <span class="brand-dot"></span>
      <span class="brand-name">LUMORA</span>
    </div>
    <p class="brand-url">www.lumoraweb.com</p>

    <h2 class="tagline">Web Design Consultancy</h2>

    <h1 class="person-name">Thomas Wren</h1>

    <address class="address contact">
      <span>address line 1</span>
      <span>address line 2</span>
      <span>address line 3</span>
    </address>

    <p class="phone contact">Tel: 01234 567890</p>
    <p class="email contact">email: name@lumoraweb.com</p>
  </main>
</body>
</html>
```